Social Action Network Needs Banner Ads for Cause T-Shirts

Hope in Hand is a social action network that transforms ordinary internet actions into donations to non-profit organizations fighting for a better tomorrow. Users can donate their social influence, print coupons, accept free offers or shop online and every action benefits causes they love. You can watch a video here: http://www.hopeinhand.example/

We are about to launch a line of cause tees that benefit the various causes we support. We want the banner ads to be positive, uplifting, inspiring and attractive. We want the ads to incorporate the following wording (although, we encourage creativity): Dress better so others can live better.

We require typical banner ad sizes: 300 x 250, 160 x 600, 728 x 90 (more sizes would be much appreciated).

Please try to include the Hope in Hand logo (color can be changed based on ad design).

In case it helps, here is a link to a page we have set up for one of our partner charities: http://www.hopeinhand.example/KindnessWells

Target Market(s)

While 80% of our users are women, we need to appeal to both.

Industry/Entity Type

Non-Profit

Requirements
Must have
• Hope in Hand logo and T-shirt design (with or without model). Also, some sort of call to action button - get tees, take action, buy now, check it out, learn more, etc.
Nice to have
• Feature the woman's tees and if possible the man's tees could be somewhere smaller in the background (if design allows).

```html
<!DOCTYPE html>
<html lang="en">
<head>
<meta charset="utf-8">
<title>Hope in Hand – Cause Tees Banner</title>
<link rel="stylesheet" href="https://fonts.googleapis.com/css2?family=Oswald:wght@500;600;700&display=swap">
<style>
  :root {
    --sky: #1ec6ef;
    --white: #ffffff;
    --cta-yellow: #f4f20d;
    --photo-light: #3b86d0;
    --photo-dark: #1f3550;
  }
  html, body {
    margin: 0;
    padding: 0;
    overflow: hidden;
    background: var(--sky);
  }
  .banner {
    position: relative;
    width: 1200px;
    height: 148px;
    background: var(--sky);
    overflow: hidden;
    font-family: "Oswald", "Arial Narrow", sans-serif;
    color: var(--white);
  }
  .model-photo {
    position: absolute;
    left: 668px;
    top: 0;
    width: 190px;
    height: 148px;
    background: linear-gradient(160deg, var(--photo-dark) 0%, var(--photo-light) 45%, var(--photo-light) 75%, var(--photo-dark) 100%);
  }
  .headline {
    position: absolute;
    left: 14px;
    top: 50px;
    margin: 0;
    font-weight: 600;
    text-transform: uppercase;
    white-space: nowrap;
    line-height: 1;
    letter-spacing: 0.2px;
    z-index: 1;
  }
  .headline .big { font-size: 42px; }
  .headline .small { font-size: 30px; }
  .headline .underlined {
    font-size: 42px;
    text-decoration: underline;
    text-decoration-thickness: 3px;
    text-underline-offset: 7px;
  }
  .cta {
    position: absolute;
    left: 874px;
    top: 56px;
    font-size: 23px;
    font-weight: 500;
    font-style: italic;
    color: var(--cta-yellow);
    text-transform: uppercase;
    text-decoration: underline;
    text-decoration-thickness: 2px;
    text-underline-offset: 4px;
    white-space: nowrap;
  }
  .brand {
    position: absolute;
    left: 1046px;
    top: 44px;
    display: flex;
    align-items: center;
    gap: 10px;
  }
  .brand-dot {
    flex: none;
    width: 20px;
    height: 20px;
    border-radius: 50%;
    background: var(--white);
  }
  .brand-name {
    font-size: 22px;
    font-weight: 600;
    color: var(--white);
    text-transform: uppercase;
    line-height: 1.1;
    width: 120px;
  }
</style>
</head>
<body>
  <div class="banner">
    <div class="model-photo" role="img" aria-label="Photo of a woman wearing a blue cause tee"></div>
    <h1 class="headline">
      <span class="big">Dress better</span>
      <span class="small">so others can</span>
      <span class="underlined">Live</span>
      <span class="big">better.</span>
    </h1>
    <div class="cta">Learn more »</div>
    <div class="brand">
      <span class="brand-dot"></span>
      <span class="brand-name">Hope in Hand</span>
    </div>
  </div>
</body>
</html>
```